Roadside building business signage for a holistic health clinic.

Replace signs as shown in the attached file. They are perforated stickers that go on the windows as shown. Looking for something that has our logo and says the name of the practice with logo (Fernbrook Health & Wellness) also boldly says Acupuncture, IV Vitamins, and Holistic Health.
Possibly our phone number as well 538-207-6145

Please don't use pink except the logo. Earthy, organic tone colors appreciated.

Need of eye catching window signage of a holistic clinic on a brick building. Pink, purple, sage green, white color. Logo is pink on a white background. Please don't overload with too much pink. Words to include are "Fernbrook Health and Wellness(name of business)", "Direct Primary Care", " Medical acupuncture", "IV Vitamin Therapy", "fernbrookwholecare-example.com","538-207-6145".

Target Market(s)

People will see in their cars passing by the building. Busy roadside so need to be visible while passing in fast speed.

Industry/Entity Type

Health & Wellness

Font styles to use
Sans Serif

Colors

Designer to choose colors to be used in the design.

Requirements
Must have
• On sign must have words Holistic Medicine, Medical Acupuncture, Direct Primary Care and IV vitamins.
Nice to have
• Simple, minimalistic, artistic yet has clear message. White, Black, Violet, Pink (logo), Dark green, Sage green.
Should not have
• Bold colors (red, yellow, blue), same tone colors. Blue waves on the current signage (uploaded file) must go.

```html
<!DOCTYPE html>
<html lang="en">
<head>
<meta charset="utf-8">
<title>Fernbrook Health &amp; Wellness – Window Banner</title>
<link rel="stylesheet" href="https://fonts.googleapis.com/css2?family=Montserrat:wght@500;600;700&display=swap">
<style>
  :root {
    --stage: #3e3e3e;
    --banner-white: #ffffff;
    --sage: #c9d6c3;
    --sage-soft: #e8efe4;
    --sage-mid: #9fb59a;
    --violet: #6b4c8a;
    --violet-soft: #b7a3cc;
    --forest: #1f4a3a;
    --logo-pink: #d9487f;
    --ink: #1e1e1e;
    --bar: rgba(205, 210, 202, 0.85);
    --bar-line: #9aa396;
  }
  * { margin: 0; padding: 0; box-sizing: border-box; }
  html, body {
    width: 1200px; height: 900px; overflow: hidden;
    background: var(--stage);
    font-family: "Montserrat", Arial, sans-serif;
  }
  .banner {
    position: absolute; left: 86px; top: 194px;
    width: 1028px; height: 428px; overflow: hidden;
    background:
      radial-gradient(ellipse 420px 260px at 120px 120px, var(--sage) 0%, transparent 70%),
      radial-gradient(ellipse 380px 200px at 260px 400px, var(--sage) 0%, transparent 75%),
      linear-gradient(90deg, var(--sage-soft) 0%, #f3f6f1 45%, var(--banner-white) 65%);
  }
  .brand-seal {
    position: absolute; left: -70px; top: -120px;
    width: 230px; height: 230px; border-radius: 50%;
    background: var(--banner-white);
    border: 6px solid var(--sage-mid);
  }
  .brand-name {
    position: absolute; left: 8px; top: 24px; width: 110px;
    text-align: center; color: var(--logo-pink);
    font-size: 12px; line-height: 1.3; font-weight: 700;
  }
  .headline {
    position: absolute; left: 60px; top: 60px; width: 530px;
    text-align: center; color: var(--forest); font-weight: 700;
  }
  .headline .line-one { display: block; font-size: 36px; line-height: 48px; letter-spacing: 0.5px; }
  .headline .line-two { display: block; font-size: 24px; line-height: 40px; font-weight: 600; }
  .accent { color: var(--violet); }
  .pills {
    position: absolute; left: 118px; top: 163px; width: 403px;
    list-style: none;
  }
  .pill {
    height: 44px; border-radius: 14px; margin-bottom: 14px;
    color: var(--banner-white); font-size: 23px; font-weight: 700;
    line-height: 44px; text-align: center; letter-spacing: 0.5px;
    white-space: nowrap;
  }
  .pill--forest { background: var(--forest); }
  .pill--violet { background: var(--violet); }
  .contact-bar {
    position: absolute; left: 0; top: 365px; width: 100%; height: 39px;
    background: var(--bar);
    display: flex; align-items: center;
    font-size: 13px; font-weight: 500; color: var(--ink);
  }
  .contact-bar span { padding: 0 14px; border-right: 1px solid var(--bar-line); line-height: 39px; white-space: nowrap; }
  .contact-bar .phone { padding-left: 60px; }
  .contact-bar span:last-child { border-right: none; }
  .hero-art {
    position: absolute; left: 586px; top: 20px;
    width: 430px; height: 340px;
    background: radial-gradient(ellipse at 50% 45%, var(--violet-soft) 0%, var(--sage-mid) 55%, rgba(159,181,154,0.2) 85%, transparent 100%);
    border-radius: 45% 45% 20% 20%;
  }
</style>
</head>
<body>
  <section class="banner">
    <div class="brand-seal"></div>
    <p class="brand-name">Fernbrook<br>Health &amp;<br>Wellness</p>

    <h1 class="headline">
      <span class="line-one">HOLISTIC <span class="accent">MEDICINE</span></span>
      <span class="line-two">at Fernbrook Health <span class="accent">&amp; Wellness</span></span>
    </h1>

    <ul class="pills">
      <li class="pill pill--forest">DIRECT PRIMARY CARE</li>
      <li class="pill pill--violet">MEDICAL ACUPUNCTURE</li>
      <li class="pill pill--forest">IV VITAMIN THERAPY</li>
    </ul>

    <div class="hero-art" role="img" aria-label="Person seated in a calm meditation pose in front of a large flower decoration"></div>

    <div class="contact-bar">
      <span class="phone">538-207-6145</span>
      <span class="address">4172 N. Harbor Rd. STE 2B Ashford, Indiana 46290</span>
      <span class="web">www.fernbrookwholecare-example.com</span>
    </div>
  </section>
</body>
</html>
```